RZ Advisory Business Cards - High End AV / Low Voltage Company

We are low voltage AV company that specializes in high end clients on the residential side and larger businesses on the commercial side. We want something modern, tech looking but also something that is extremely professional looking. We have uploaded our logos and postcards we already have in the field. Along with a picture of one of our wrapped vans. Our website is at www.rzadvisory.example and our primary colors are the orange, green, grey and blue all military color finishes.

We are interesting in the slogans "Matching You with the Ideal Equipment" or "Guiding the Harborlands in Tech"

Target Market(s)

We focus on 70% Commercial and 30% Residential Customers

Industry/Entity Type

Low Voltage, AV Company

Contact Information for Business Card

Name - Dorian Fenwick, Title - Owner, Office Phone - 555-402-7163, Mobile Phone - 555-718-3094, E-Mail - t@rzadvisory.example, Website: www.rzadvisory.example

Font styles to use
Sans Serif

Requirements
Must have
• Must have Name, Title, Work Phone & Mobile, Website and Logo.
Nice to have
• We want something that will impress our higher end clients with a great logo
Should not have
• Too traditional or plain.

```html
<!DOCTYPE html>
<html lang="en">
<head>
<meta charset="UTF-8">
<title>RZ Advisory Business Card</title>
<link rel="stylesheet" href="https://fonts.googleapis.com/css2?family=Montserrat:wght@500;600&family=Open+Sans:wght@400;500;700&display=swap">
<style>
  :root {
    --stage: #8a8a8c;
    --olive: #4a5427;
    --olive-deep: #3d4720;
    --olive-light: #56622f;
    --orange: #ec6a35;
    --ink: #2f3817;
    --paper: #ffffff;
  }
  * { margin: 0; padding: 0; box-sizing: border-box; }
  html, body { width: 900px; height: 1200px; overflow: hidden; }
  body { background: var(--stage); position: relative; font-family: "Open Sans", sans-serif; }

  .card {
    position: absolute;
    left: 135px;
    width: 630px;
    height: 357px;
    border-radius: 12px;
    overflow: hidden;
  }
  .card--front { top: 215px; background: var(--olive); }
  .card--back { top: 629px; background: var(--paper); }

  .front__texture {
    position: absolute; inset: 0;
    background: radial-gradient(ellipse at 75% 50%, var(--olive-light) 0%, var(--olive) 45%, var(--olive-deep) 100%);
  }
  .front__brand {
    position: absolute; left: 0; right: 0; top: 70px;
    display: flex; flex-direction: column; align-items: center; gap: 18px;
  }
  .brand-ring {
    width: 110px; height: 110px; border-radius: 50%;
    border: 6px solid var(--orange);
  }
  .brand-name {
    font-family: "Montserrat", sans-serif; font-weight: 600;
    color: var(--orange); font-size: 34px; letter-spacing: 3px; text-transform: uppercase;
  }
  .front__tagline {
    position: absolute; left: 0; right: 0; top: 315px;
    display: flex; align-items: center; justify-content: center; gap: 10px;
  }
  .tagline-rule { width: 52px; height: 2px; background: var(--orange); position: relative; }
  .tagline-rule::after {
    content: ""; position: absolute; top: -2.5px; width: 7px; height: 7px;
    border-radius: 50%; background: var(--orange);
  }
  .tagline-rule--left::after { left: -2px; }
  .tagline-rule--right::after { right: -2px; }
  .tagline-text {
    font-family: "Montserrat", sans-serif; font-weight: 600;
    color: #fff; font-size: 14px; letter-spacing: 0.3px; text-transform: uppercase;
  }

  .back__brand {
    position: absolute; left: 350px; top: 36px; width: 194px;
    display: flex; flex-direction: column; align-items: center; gap: 10px;
  }
  .back__brand .brand-ring { width: 92px; height: 92px; border-width: 5px; }
  .back__brand .brand-name { font-size: 20px; letter-spacing: 2px; }

  .holder { position: absolute; left: 56px; top: 165px; }
  .holder__name { font-weight: 700; font-size: 25px; color: var(--ink); }
  .holder__title { font-size: 15px; color: var(--orange); letter-spacing: 0.5px; margin-top: 2px; }

  .contact { position: absolute; left: 366px; top: 225px; list-style: none; }
  .contact__item {
    display: flex; align-items: center; gap: 7px; height: 25.5px;
    font-size: 15px; color: var(--ink); letter-spacing: 0.6px;
  }
  .contact__item--phone { letter-spacing: 2.2px; }
  .contact__icon { width: 14px; height: 14px; flex: none; }
</style>
</head>
<body>
  <section class="card card--front">
    <div class="front__texture" role="img" aria-label="Embossed repeating brand-mark pattern in tonal olive green"></div>
    <div class="front__brand">
      <div class="brand-ring"></div>
      <div class="brand-name">RZ Advisory</div>
    </div>
    <div class="front__tagline">
      <span class="tagline-rule tagline-rule--left"></span>
      <span class="tagline-text">Matching You with the Ideal Equipment</span>
      <span class="tagline-rule tagline-rule--right"></span>
    </div>
  </section>

  <section class="card card--back">
    <div class="back__brand">
      <div class="brand-ring"></div>
      <div class="brand-name">RZ Advisory</div>
    </div>
    <div class="holder">
      <h1 class="holder__name">Dorian Fenwick</h1>
      <p class="holder__title">Owner</p>
    </div>
    <ul class="contact">
      <li class="contact__item contact__item--phone">
        <svg class="contact__icon" viewBox="0 0 24 24"><path fill="#ec6a35" d="M6.6 10.8a15 15 0 0 0 6.6 6.6l2.2-2.2c.3-.3.7-.4 1-.2 1.1.4 2.3.6 3.6.6.6 0 1 .4 1 1V20c0 .6-.4 1-1 1A17 17 0 0 1 3 4c0-.6.4-1 1-1h3.5c.6 0 1 .4 1 1 0 1.3.2 2.5.6 3.6.1.3 0 .7-.2 1z"/></svg>
        555-402-7163
      </li>
      <li class="contact__item contact__item--phone">
        <svg class="contact__icon" viewBox="0 0 24 24"><rect x="6" y="1.5" width="12" height="21" rx="2" fill="none" stroke="#ec6a35" stroke-width="2.4"/><circle cx="12" cy="18.5" r="1.3" fill="#ec6a35"/></svg>
        555-718-3094
      </li>
      <li class="contact__item">
        <svg class="contact__icon" viewBox="0 0 24 24"><rect x="2" y="5" width="20" height="14" rx="1.5" fill="#ec6a35"/><path d="M3 6l9 7 9-7" fill="none" stroke="#fff" stroke-width="1.8"/></svg>
        t@rzadvisory.example
      </li>
      <li class="contact__item">
        <svg class="contact__icon" viewBox="0 0 24 24"><g fill="none" stroke="#ec6a35" stroke-width="2"><circle cx="12" cy="12" r="9.5"/><ellipse cx="12" cy="12" rx="4" ry="9.5"/><path d="M2.5 12h19M4 7h16M4 17h16"/></g></svg>
        www.rzadvisory.example
      </li>
    </ul>
  </section>
</body>
</html>
```